RWT General Contracting

Roofing, Siding,windows, doors, Gutter,additions, decks, garagesand hanyman services fully insured and licensed, free estimates, accept all major credit cards call (617)442-9073 email morvinkt@mailbrook.net

Target Market(s)

Home improvement

Industry/Entity Type

Home Improvement

Requirements
Must have
• Whats listed above
Nice to have
• I dont have a logo i want wording for roofing, siding, gutter, decks, additions, windows, doors, and handyman services with my phone # 617-442-9073 and email morvinkt@mailbrook.net

```html
<!DOCTYPE html>
<html lang="en">
<head>
<meta charset="utf-8">
<title>RWT General Contracting – Postcard</title>
<link rel="stylesheet" href="https://fonts.googleapis.com/css2?family=Orbitron:wght@700;800&family=Anton&family=Lato:wght@400&display=swap">
<style>
  :root {
    --page-bg: #ebe8e3;
    --frame-blue: #2e6fe3;
    --figure-blue: #2d6ee6;
    --card-black: #000000;
    --headline-yellow: #f6e31c;
    --call-gold: #f1c232;
    --text-white: #ffffff;
    --back-white: #ffffff;
    --rule-grey: #a9a9a9;
    --stamp-grey: #9b9b9b;
  }
  html, body {
    margin: 0;
    padding: 0;
    width: 1200px;
    height: 508px;
    overflow: hidden;
    background: var(--page-bg);
  }
  .canvas {
    position: relative;
    width: 1200px;
    height: 508px;
  }
  .postcard-front {
    position: absolute;
    left: 62px;
    top: 44px;
    width: 516px;
    height: 400px;
    background: var(--frame-blue);
  }
  .front-panel {
    position: absolute;
    left: 8px;
    top: 8px;
    right: 8px;
    bottom: 8px;
    background: var(--card-black);
  }
  .worker-figure {
    position: absolute;
    left: 22px;
    top: 22px;
    width: 104px;
    height: 338px;
    background: linear-gradient(180deg, var(--figure-blue), #2258c4);
    border-radius: 52px 52px 6px 6px;
  }
  .service-list {
    position: absolute;
    left: 132px;
    top: 25px;
    margin: 0;
    padding: 0;
    list-style: none;
    font-family: "Orbitron", sans-serif;
    font-weight: 800;
    font-size: 20px;
    letter-spacing: 3.4px;
    line-height: 25px;
    color: var(--text-white);
    white-space: nowrap;
  }
  .service-list .dot {
    display: inline-block;
    width: 7px;
    height: 7px;
    border-radius: 50%;
    background: var(--text-white);
    vertical-align: middle;
    margin: 0 6px 3px 0;
  }
  .service-list .dot.mid { margin-left: 4px; }
  .headline {
    position: absolute;
    left: 140px;
    top: 158px;
    margin: 0;
    font-family: "Anton", sans-serif;
    font-weight: 400;
    font-size: 46px;
    line-height: 56px;
    letter-spacing: 4px;
    color: var(--headline-yellow);
    white-space: nowrap;
  }
  .credentials {
    position: absolute;
    left: 198px;
    top: 227px;
    margin: 0;
    padding: 0;
    list-style: none;
    font-family: "Lato", sans-serif;
    font-size: 14.5px;
    line-height: 18px;
    color: var(--headline-yellow);
  }
  .credentials li { display: flex; align-items: center; gap: 4px; }
  .credentials svg { width: 13px; height: 13px; }
  .tagline, .call-line {
    position: absolute;
    left: 155px;
    margin: 0;
    font-family: "Orbitron", sans-serif;
    font-weight: 700;
    font-size: 19px;
    white-space: nowrap;
  }
  .tagline { top: 273px; letter-spacing: 4.6px; color: var(--text-white); }
  .call-line { top: 309px; letter-spacing: 3.6px; color: var(--call-gold); }
  .email-line {
    position: absolute;
    left: 224px;
    top: 341px;
    margin: 0;
    font-family: "Lato", sans-serif;
    font-size: 14px;
    color: var(--text-white);
    display: flex;
    align-items: center;
    gap: 5px;
  }
  .email-line svg { width: 14px; height: 11px; }
  .postcard-back {
    position: absolute;
    left: 620px;
    top: 52px;
    width: 516px;
    height: 400px;
    background: var(--back-white);
  }
  .stamp-box {
    position: absolute;
    left: 387px;
    top: 20px;
    width: 90px;
    height: 90px;
    box-sizing: border-box;
    border: 2px dashed var(--stamp-grey);
  }
  .address-rule {
    position: absolute;
    left: 250px;
    width: 230px;
    height: 0;
    border-top: 1.5px solid var(--rule-grey);
  }
</style>
</head>
<body>
<div class="canvas">
  <section class="postcard-front">
    <div class="front-panel">
      <div class="worker-figure" role="img" aria-label="Blue silhouette of a contractor in a hard hat with a tool belt"></div>
      <ul class="service-list">
        <li><span class="dot"></span>ROOFING<span class="dot mid"></span>SIDING</li>
        <li><span class="dot"></span>WINDOWS<span class="dot mid"></span>DOORS</li>
        <li><span class="dot"></span>GUTTER<span class="dot mid"></span>ADDITIONS</li>
        <li><span class="dot"></span>DECKS<span class="dot mid"></span>GARAGES</li>
        <li><span class="dot"></span>HANDYMAN SERVICES</li>
      </ul>
      <h1 class="headline">FREE ESTIMATES</h1>
      <ul class="credentials">
        <li><svg viewBox="0 0 12 12"><path d="M1 6.5 L4.5 10 L11 1.5" fill="none" stroke="currentColor" stroke-width="2.2"/></svg>Fully insured and Licensed</li>
        <li><svg viewBox="0 0 12 12"><path d="M1 6.5 L4.5 10 L11 1.5" fill="none" stroke="currentColor" stroke-width="2.2"/></svg>Accepts All Major Credit Cards</li>
      </ul>
      <p class="tagline">NO JOB TOO SMALL</p>
      <p class="call-line">CALL (617)442-9073</p>
      <p class="email-line"><svg viewBox="0 0 14 11"><rect x="0.6" y="0.6" width="12.8" height="9.8" fill="none" stroke="currentColor" stroke-width="1.2"/><path d="M0.6 0.6 L7 6 L13.4 0.6" fill="none" stroke="currentColor" stroke-width="1.2"/></svg>morvinkt@mailbrook.net</p>
    </div>
  </section>

  <section class="postcard-back">
    <div class="stamp-box"></div>
    <div class="address-rule" style="top:174px"></div>
    <div class="address-rule" style="top:206px"></div>
    <div class="address-rule" style="top:238px"></div>
    <div class="address-rule" style="top:269px"></div>
  </section>
</div>
</body>
</html>
```